Brochure design for HVAC Company

A classic tri-fold brochure design for an air conditioning, refrigeration, and heating company. Would like the designs to be simple (uncluttered), professional, and pull in the logo colors. Attached is the logo and a business card designs. The company name is Bluefinch Ridge Air Conditioning, Refrigeration, and Heating.

Target Market(s)

Businesses normally food establishments for refrigeration and ice machines. Looking to sell them on maintenance plan: Gold, Silver, and Bronze. The material should help them to understand the services offered: Maintenance, Servicing and Troubleshooting, and Installations of ice machines, commercial refrigeration, and walk-in freezers and air conditioning (duct, ductless, and rooftop)

Industry/Entity Type

Hvac

Font styles to use
Sans Serif

Requirements
Must have
• Include standard information, such as company name, at least two types of contact information (phone, email and post office address), a logo and tagline. It should also include a headline on the front and two or three brief items outlining benefits your organization can provide.
• Tagline is approximately 14 words and 66 characters.
• Looking to inform customers of services offered: maintenance three plans gold, silver, and bronze, servicing and troubleshooting, and installation.
• Products Serviced, maintained, and installed: Commercial refrigeration, Ice Machines, Air Conditioning (both duct, ductless, and rooftop), walk in freezers.
• Call to action is $100 off on signed maintenance contract. $50 off on first service call.
• Use lorem ipsum text to complement the details of the above information. I will add it later before printing.
• Use logo color scheme and any other colors that complement it.
• Would like this to be a word template.
Nice to have
• Can you make this a Microsoft Word template? Sketch is good, or adobe cs4 format.
Should not have
• Photos should NOT be focused on the homeowner. Should BE focused on the commercial side of the business. Photos can be from any of these product areas: commercial refrigeration, ice machine, walk in freezer boxes, and light roof top ac and heating units.

```html
<!DOCTYPE html>
<html lang="en">
<head>
<meta charset="utf-8">
<title>Bluefinch Ridge Tri-fold Brochure</title>
<link href="https://fonts.googleapis.com/css2?family=Oswald:wght@400;500;600;700&family=Lato:wght@400;700;900&display=swap" rel="stylesheet">
<style>
:root{
  --orange:#f26a21;
  --orange-dark:#c94f12;
  --blue:#1f4fb0;
  --blue-dark:#153a86;
  --ink:#2b2b2b;
  --grey-text:#5a5a5a;
  --paper:#ffffff;
  --stage:#e4e4e4;
  --gold:#a38d2c;
  --gold-light:#e3cf6a;
  --silver:#4f4f4f;
  --silver-light:#c9c9c9;
  --bronze:#7b5a3b;
  --bronze-light:#d8b894;
}
*{box-sizing:border-box;margin:0;padding:0}
html,body{width:800px;height:1200px;overflow:hidden}
body{background:var(--stage);font-family:'Lato',sans-serif;color:var(--ink);position:relative}
.spread{position:absolute;left:30px;width:740px;height:572px;background:var(--paper);box-shadow:0 2px 10px rgba(0,0,0,.18);overflow:hidden}
.spread--outside{top:22px}
.spread--inside{top:608px}
.fold{position:absolute;top:0;bottom:0;width:1px;background:rgba(0,0,0,.06)}
.layer{position:absolute;left:0;top:0;width:740px;height:572px}
.heading{font-family:'Oswald',sans-serif;font-weight:600;letter-spacing:.5px}

/* outside - benefits panel */
.benefits{position:absolute;left:22px;top:24px;width:205px;color:#fff}
.benefits__title{font-size:20px;margin-bottom:14px}
.benefits__list{list-style:none}
.benefits__item{position:relative;padding-left:14px;font-size:8.2px;line-height:1.45;margin-bottom:16px}
.benefits__item::before{content:"";position:absolute;left:0;top:4px;width:5px;height:5px;border-radius:50%;background:#fff}

.offer{position:absolute;left:0;width:247px;height:58px;display:flex;align-items:center}
.offer--orange{top:392px}
.offer--blue{top:466px}
.offer__badge{margin-left:16px;width:72px;height:46px;background:#fff;border:3px solid var(--ink);font-family:'Oswald',sans-serif;font-weight:700;font-size:17px;line-height:.95;text-align:center;display:flex;align-items:center;justify-content:center;color:var(--ink)}
.offer__text{flex:1;text-align:center;color:#fff;font-family:'Oswald',sans-serif;font-weight:500;font-size:12px;line-height:1.1;text-transform:uppercase;padding-right:8px}

/* outside - contact panel */
.contact{position:absolute;left:247px;top:410px;width:247px;text-align:center;font-size:10px;color:var(--ink)}
.contact__row{margin-bottom:8px;display:flex;flex-direction:column;align-items:center;gap:2px}
.contact__icon{width:10px;height:10px}

/* outside - cover */
.brand{position:absolute;left:560px;top:26px;width:150px;height:40px;background:#fff;display:flex;align-items:center;gap:6px;padding:0 8px;box-shadow:0 2px 4px rgba(0,0,0,.12)}
.brand__dot{width:14px;height:14px;border-radius:50%;background:var(--orange);flex:none}
.brand__name{font-family:'Oswald',sans-serif;font-weight:600;font-size:10px;line-height:1.1;color:var(--blue)}
.cover{position:absolute;left:500px;top:360px;width:225px;text-align:right}
.cover__headline{font-family:'Oswald',sans-serif;font-weight:600;font-size:30px;color:var(--blue);line-height:1}
.cover__sub{font-size:13px;color:var(--grey-text);margin-top:2px}
.cover__accent{font-family:'Oswald',sans-serif;font-weight:700;font-size:25px;color:var(--orange);line-height:1.05}
.cover__small{font-size:10.5px;color:var(--grey-text)}
.cover__url{display:inline-block;margin-top:8px;background:var(--blue);color:#fff;font-weight:700;font-size:10px;padding:4px 12px 4px 40px}

/* inside - plans */
.plans{position:absolute;left:18px;top:22px;width:215px}
.plans__title{font-size:18px;color:var(--blue);margin-bottom:6px}
.plan{position:relative;margin-bottom:30px;border:2px solid var(--ink);background:#fff;box-shadow:3px 3px 0 rgba(0,0,0,.15)}
.plan__head{position:relative;height:24px}
.plan__bar{position:absolute;left:0;top:10px;right:0;height:14px;padding-left:6px;font-family:'Lato',sans-serif;font-weight:900;font-size:9px;line-height:14px;color:var(--ink)}
.plan__price{position:absolute;right:-2px;top:-14px;width:90px;height:24px;border-radius:10px 0 0 0;color:#fff;font-family:'Oswald',sans-serif;font-size:15px;text-align:center;line-height:24px}
.plan__body{font-size:6.8px;line-height:1.4;padding:6px 8px 8px;color:var(--grey-text)}
.plan--gold .plan__bar{background:linear-gradient(90deg,var(--gold-light),#f5ebb6)}
.plan--gold .plan__price{background:var(--gold)}
.plan--silver .plan__bar{background:linear-gradient(90deg,var(--silver-light),#eee)}
.plan--silver .plan__price{background:var(--silver)}
.plan--bronze .plan__bar{background:linear-gradient(90deg,var(--bronze-light),#f3e5d4)}
.plan--bronze .plan__price{background:var(--bronze)}

/* inside - services */
.services{position:absolute;left:262px;top:22px;width:220px}
.services__title{font-size:17px;color:var(--orange)}
.services__group{font-size:12px;font-weight:700;color:var(--blue);margin:4px 0 3px}
.services__list{list-style:none;margin-bottom:10px}
.services__item{position:relative;padding-left:14px;font-size:7.4px;margin-bottom:5px;color:var(--ink)}
.services__item::before{content:"";position:absolute;left:0;top:0;width:8px;height:8px;border-radius:50%;background:var(--blue)}
.services__item::after{content:"";position:absolute;left:3px;top:2px;width:2px;height:3px;border:solid #fff;border-width:0 1.2px 1.2px 0;transform:rotate(45deg)}

/* inside - installed */
.installed{position:absolute;left:506px;top:22px;width:218px}
.installed__title{font-size:12px;font-weight:700;color:var(--blue);margin-bottom:8px}
.product{display:flex;gap:8px;margin-bottom:12px}
.product__icon{flex:none;width:20px;height:20px;border-radius:50%;border:2px solid var(--orange);display:flex;align-items:center;justify-content:center}
.product__icon span{width:8px;height:8px;background:var(--orange);border-radius:2px}
.product__name{font-size:7.6px;font-weight:900;color:var(--ink)}
.product__name em{font-style:normal;color:var(--orange)}
.product__text{font-size:6.8px;line-height:1.4;color:var(--grey-text)}
</style>
</head>
<body>

<!-- OUTSIDE SPREAD -->
<section class="spread spread--outside" aria-label="Brochure outside">
  <div class="fold" style="left:247px"></div>
  <div class="fold" style="left:494px"></div>
  <svg class="layer" viewBox="0 0 740 572" aria-hidden="false">
    <defs>
      <linearGradient id="coverPhoto" x1="0" y1="0" x2="1" y2="1">
        <stop offset="0" stop-color="#f3f3f3"/>
        <stop offset=".6" stop-color="#e2dedc"/>
        <stop offset="1" stop-color="#b9b4b6"/>
      </linearGradient>
    </defs>
    <g role="img" aria-label="Photo: client relaxing on a sofa in a cooled room, wall-mounted air conditioner above">
      <path d="M247,0 H740 V270 C620,300 540,335 420,345 C350,350 290,340 247,335 Z" fill="url(#coverPhoto)"/>
    </g>
    <path d="M0,0 H247 V360 C170,380 90,395 0,400 Z" fill="var(--orange)"/>
    <path d="M0,400 C90,395 170,380 247,360 C290,340 350,350 420,345 C540,335 620,300 740,270" fill="none" stroke="var(--blue)" stroke-width="4"/>
    <path d="M0,408 C90,403 170,388 247,368 C290,350 350,358 420,353 C540,343 620,308 740,280" fill="none" stroke="var(--blue)" stroke-width="1.2"/>
    <path d="M0,392 L190,392 L247,380 L247,450 L0,450 Z" fill="var(--orange)"/>
    <path d="M70,392 L190,392 L140,450 L70,450 Z" fill="var(--orange-dark)" opacity=".55"/>
    <path d="M0,466 L247,444 L247,524 L0,524 Z" fill="var(--blue)"/>
    <path d="M70,466 L200,455 L150,524 L70,524 Z" fill="var(--blue-dark)" opacity=".5"/>
  </svg>

  <div class="benefits">
    <h2 class="benefits__title heading">OUR BENEFITS:</h2>
    <ul class="benefits__list">
      <li class="benefits__item">Lorem ipsum dolor sit amet, consectetur adipiscing elit. Ut nisi tortor, egestas vel vulputate non, pulvinar eget sem. Curabitur ipsum metus, hendrerit vel diam semper, dignissim mollis dui. Donec vitae eleifend nibh. Maecenas risus nulla, viverra vel lacinia ut.</li>
      <li class="benefits__item">Lorem ipsum dolor sit amet, consectetur adipiscing elit. Ut nisi tortor, egestas vel vulputate non, pulvinar eget sem. Curabitur ipsum metus, hendrerit vel diam semper, dignissim mollis dui. Donec vitae eleifend nibh. Maecenas risus nulla, viverra vel lacinia ut.</li>
      <li class="benefits__item">Lorem ipsum dolor sit amet, consectetur adipiscing elit. Ut nisi tortor, egestas vel vulputate non, pulvinar eget sem. Curabitur ipsum metus, hendrerit vel diam semper, dignissim mollis dui. Donec vitae eleifend nibh. Maecenas risus nulla, viverra vel lacinia ut.</li>
      <li class="benefits__item">Lorem ipsum dolor sit amet, consectetur adipiscing elit. Ut nisi tortor, egestas vel vulputate non, pulvinar eget sem. Curabitur ipsum metus, hendrerit vel diam semper, dignissim mollis dui. Donec vitae eleifend nibh.</li>
    </ul>
  </div>

  <div class="offer offer--orange">
    <div class="offer__badge">$100<br>OFF</div>
    <div class="offer__text">On signed<br>maintenance contract</div>
  </div>
  <div class="offer offer--blue">
    <div class="offer__badge">$50<br>OFF</div>
    <div class="offer__text">On first<br>service call</div>
  </div>

  <div class="contact">
    <div class="contact__row">
      <svg class="contact__icon" viewBox="0 0 10 10"><path d="M2,1 L4,1 L4.6,3 L3.5,3.8 C4,5 5,6 6.2,6.5 L7,5.4 L9,6 L9,8 C5,8.5 1.5,5 2,1 Z" fill="var(--orange)"/></svg>
      <span>631-555-0142</span>
    </div>
    <div class="contact__row">
      <svg class="contact__icon" viewBox="0 0 10 10"><rect x="1" y="2.5" width="8" height="5.5" fill="var(--orange)"/><path d="M1,2.5 L5,5.5 L9,2.5" fill="none" stroke="#fff" stroke-width=".8"/></svg>
      <span>hello@bluefinchridge.com</span>
    </div>
    <div class="contact__row">
      <svg class="contact__icon" viewBox="0 0 10 10"><circle cx="5" cy="5" r="4" fill="var(--orange)"/><path d="M1,5 H9 M5,1 C3,3 3,7 5,9 M5,1 C7,3 7,7 5,9" fill="none" stroke="#fff" stroke-width=".6"/></svg>
      <span>www.bluefinchridgehvac.com</span>
    </div>
    <div class="contact__row">
      <svg class="contact__icon" viewBox="0 0 10 10"><path d="M5,9.5 C2,6 1.8,4.5 1.8,3.8 A3.2,3.2 0 0 1 8.2,3.8 C8.2,4.5 8,6 5,9.5 Z" fill="var(--orange)"/><circle cx="5" cy="3.8" r="1.2" fill="#fff"/></svg>
      <span>PO Box 218<br>Millbrook, NY 11790</span>
    </div>
  </div>

  <div class="brand">
    <span class="brand__dot"></span>
    <span class="brand__name">Bluefinch Ridge Air Conditioning, Refrigeration, and Heating</span>
  </div>

  <div class="cover">
    <h1 class="cover__headline">LOREM IPSUM</h1>
    <p class="cover__sub">dolor sit amet, consectetur</p>
    <p class="cover__accent">ADIPISCING ELIT.UT</p>
    <p class="cover__small">nisi tortor egestas vel vulputate</p>
    <span class="cover__url">www.bluefinchridgehvac.com</span>
  </div>
</section>

<!-- INSIDE SPREAD -->
<section class="spread spread--inside" aria-label="Brochure inside">
  <div class="fold" style="left:247px"></div>
  <div class="fold" style="left:494px"></div>
  <svg class="layer" viewBox="0 0 740 572">
    <defs>
      <linearGradient id="techPhoto" x1="0" y1="0" x2="1" y2="1">
        <stop offset="0" stop-color="#c9c4c0"/>
        <stop offset=".5" stop-color="#a88a74"/>
        <stop offset="1" stop-color="#5b4a40"/>
      </linearGradient>
      <linearGradient id="unitPhoto" x1="0" y1="0" x2="1" y2="1">
        <stop offset="0" stop-color="#e8ebee"/>
        <stop offset=".55" stop-color="#b6bcc4"/>
        <stop offset="1" stop-color="#2e3f7a"/>
      </linearGradient>
    </defs>
    <g role="img" aria-label="Photo: technician checking wiring with a multimeter">
      <path d="M247,392 C330,385 420,372 494,355 V572 H247 Z" fill="url(#techPhoto)"/>
    </g>
    <g role="img" aria-label="Photo: technician servicing an outdoor condenser unit">
      <path d="M494,355 C580,335 660,305 740,265 V572 H494 Z" fill="url(#unitPhoto)"/>
    </g>
    <path d="M247,392 C330,385 420,372 494,355 C580,335 660,305 740,265" fill="none" stroke="var(--blue)" stroke-width="4"/>
    <path d="M247,384 C330,377 420,364 494,347 C580,327 660,297 740,257" fill="none" stroke="var(--blue)" stroke-width="1.2"/>
  </svg>

  <div class="plans">
    <h2 class="plans__title heading">OUR PLAN</h2>
    <article class="plan plan--gold">
      <div class="plan__head"><div class="plan__bar">Gold Plan</div><div class="plan__price">$XX</div></div>
      <p class="plan__body">Lorem ipsum dolor sit amet, consectetur adipiscing elit. Ut nisi tortor, egestas vel vulputate non, pulvinar eget sem. Curabitur ipsum metus, hendrerit vel diam semper, dignissim mollis dui. Donec vitae eleifend nibh. Maecenas risus nulla, viverra vel lacinia ut, auctor sed turpis. Etiam non mi magna. In ac mollis massa.</p>
    </article>
    <article class="plan plan--silver">
      <div class="plan__head"><div class="plan__bar">Silver Plan</div><div class="plan__price">$XX</div></div>
      <p class="plan__body">Lorem ipsum dolor sit amet, consectetur adipiscing elit. Ut nisi tortor, egestas vel vulputate non, pulvinar eget sem. Curabitur ipsum metus, hendrerit vel diam semper, dignissim mollis dui. Donec vitae eleifend nibh. Maecenas risus nulla, viverra vel lacinia ut, auctor sed turpis. Etiam non mi magna. Nunc varius dolor quis mauris convallis.</p>
    </article>
    <article class="plan plan--bronze">
      <div class="plan__head"><div class="plan__bar">Bronze Plan</div><div class="plan__price">$XX</div></div>
      <p class="plan__body">Lorem ipsum dolor sit amet, consectetur adipiscing elit. Ut nisi tortor, egestas vel vulputate non, pulvinar eget sem. Curabitur ipsum metus, hendrerit vel diam semper, dignissim mollis dui. Donec vitae eleifend nibh. Maecenas in lectus faucibus, viverra lectus non, venenatis turpis. Nunc varius dolor quis mauris convallis, vel vestibulum magna placerat.</p>
    </article>
  </div>

  <div class="services">
    <h2 class="services__title heading">OUR SERVICES</h2>
    <h3 class="services__group">Serviced</h3>
    <ul class="services__list">
      <li class="services__item">Proin id pellentesque libero, mattis suscipit neque.</li>
      <li class="services__item">Nunc a mauris vestibulum</li>
      <li class="services__item">Tempor diam et</li>
      <li class="services__item">Consequat tortor</li>
      <li class="services__item">Curabitur et nisi laoreet</li>
      <li class="services__item">Laoreet neque sit amet, facilisis dui.</li>
    </ul>
    <h3 class="services__group">Maintained</h3>
    <ul class="services__list">
      <li class="services__item">Laoreet neque sit amet, facilisis dui.</li>
      <li class="services__item">Proin id pellentesque libero, mattis suscipit neque.</li>
      <li class="services__item">Nunc a mauris vestibulum</li>
      <li class="services__item">Tempor diam et</li>
      <li class="services__item">Consequat tortor</li>
      <li class="services__item">Curabitur et nisi laoreet</li>
    </ul>
  </div>

  <div class="installed">
    <h3 class="installed__title">Installed</h3>
    <div class="product">
      <div class="product__icon"><span></span></div>
      <div><p class="product__name">Commercial refrigeration</p><p class="product__text">Lorem ipsum dolor sit amet, consectetur adipiscing elit. Ut nisi tortor, egestas vel vulputate non, pulvinar eget sem. Curabitur ipsum metus, hendrerit vel diam semper, dignissim mollis dui. Donec vitae eleifend nibh.</p></div>
    </div>
    <div class="product">
      <div class="product__icon"><span></span></div>
      <div><p class="product__name">Ice Machines</p><p class="product__text">Lorem ipsum dolor sit amet, consectetur adipiscing elit. Ut nisi tortor, egestas vel vulputate non, pulvinar eget sem. Curabitur ipsum metus, hendrerit vel diam semper, dignissim mollis dui. Donec vitae eleifend nibh.</p></div>
    </div>
    <div class="product">
      <div class="product__icon"><span></span></div>
      <div><p class="product__name">Air Conditioning <em>(both duct, ductless, and rooftop)</em></p><p class="product__text">Lorem ipsum dolor sit amet, consectetur adipiscing elit. Ut nisi tortor, egestas vel vulputate non, pulvinar eget sem. Curabitur ipsum metus, hendrerit vel diam semper, dignissim mollis dui. Donec vitae eleifend nibh.</p></div>
    </div>
    <div class="product">
      <div class="product__icon"><span></span></div>
      <div><p class="product__name">Walk in freezers</p><p class="product__text">Lorem ipsum dolor sit amet, consectetur adipiscing elit. Ut nisi tortor, egestas vel vulputate non, pulvinar eget sem. Curabitur ipsum metus, hendrerit vel diam semper.</p></div>
    </div>
  </div>
</section>

</body>
</html>
```